Business card for Velvet & Lark weddings and events management company
Velvet & Lark
Business card for Velvet & Lark weddings and events management company - Events
Creative Brief
Modern
Nargiza Huseynova
General Manager
17 Samad Str. AZ 1014, Baku, Azerbaijan
nargiza.huseynova@velvetlark-example.az
www.velvetlark-example.az
In addition to english version, be ready to provide azerbaijani version with little changes in titles as seen below: Name: Nərgizə Hüseynova Title: Müdir Address: Samad küç., 17 AZ1014, Bakı, Azərbaycan Slogan on the back: Sevindirməklə sevinirik! (as seen on azerbaijani version of logo, using only capital letters)
HAPPY TO MAKE YOU HAPPY! SEVİNDİRMƏKLƏ SEVİNİRİK! (on azerbaijani version) for this option, you can provide a different font as well, something maybe handwritten and more friendly. (Original font is Trajan Pro)
tulipwanderer tulipwanderer

```html
<!DOCTYPE html>
<html lang="en">
<head>
<meta charset="utf-8">
<title>Velvet &amp; Lark — Business Card</title>
<link rel="stylesheet" href="https://fonts.googleapis.com/css2?family=Cinzel:wght@400&family=Open+Sans:wght@400;700&display=swap">
<style>
  :root {
    --backdrop: #3a3a3a;
    --card: #ffffff;
    --ink: #1c1c1c;
    --ink-soft: #555555;
    --band-dark: #111111;
    --band-mid: #8a8a8a;
    --band-light: #c4c4c4;
  }
  * { margin: 0; padding: 0; box-sizing: border-box; }
  html, body {
    width: 1200px; height: 1078px; overflow: hidden;
    background: var(--backdrop);
  }
  .stage {
    position: relative; width: 1200px; height: 1078px;
    display: flex; flex-direction: column; align-items: center; justify-content: center; gap: 46px;
  }
  .card {
    position: relative; width: 840px; height: 480px;
    background: var(--card); color: var(--ink);
    box-shadow: 0 10px 30px rgba(0,0,0,.35);
    overflow: hidden;
  }
  .brand-name {
    font-family: "Cinzel", serif; font-weight: 400; color: var(--ink);
    letter-spacing: 4px; white-space: nowrap;
    display: flex; align-items: center; gap: 18px;
  }
  .brand-name .dot {
    width: 26px; height: 26px; border-radius: 50%; border: 2px solid var(--ink);
  }
  .tagline {
    font-family: "Cinzel", serif; color: var(--ink); text-transform: uppercase;
    letter-spacing: 3px; white-space: nowrap;
    display: flex; align-items: center; gap: 12px;
  }
  .tagline::before, .tagline::after {
    content: ""; flex: 1; height: 1px; background: var(--ink);
  }
  .heading {
    font-family: "Open Sans", sans-serif; font-weight: 700; font-size: 20px;
    letter-spacing: 1.5px; text-transform: uppercase;
  }
  .detail-list {
    list-style: none; font-family: "Open Sans", sans-serif; font-size: 15px;
    line-height: 1.5; color: var(--ink-soft); white-space: nowrap;
  }

  /* contact side */
  .card--contact .contact-block { position: absolute; left: 70px; top: 36px; }
  .card--contact .brand-lockup { position: absolute; left: 70px; top: 184px; width: 370px; }
  .card--contact .brand-name { font-size: 34px; }
  .card--contact .tagline { font-size: 12px; margin-top: 8px; padding-left: 44px; }
  .card--contact .social-block { position: absolute; left: 500px; top: 150px; width: 300px; }
  .accent-band {
    position: absolute; left: 0; top: 290px; width: 440px; height: 34px; display: flex;
  }
  .accent-band span { height: 100%; }
  .accent-band .dark { background: var(--band-dark); }
  .accent-band .mid { background: var(--band-mid); }
  .accent-band .light { background: var(--band-light); }
  .person { position: absolute; right: 60px; bottom: 70px; text-align: right; }
  .person .name { font-family: "Open Sans", sans-serif; font-weight: 700; font-size: 24px; letter-spacing: 1px; text-transform: uppercase; }
  .person .role { font-family: "Open Sans", sans-serif; font-size: 15px; letter-spacing: 1.5px; text-transform: uppercase; color: var(--ink-soft); margin-top: 4px; }

  /* brand side */
  .card--brand { display: flex; align-items: center; justify-content: center; }
  .card--brand .brand-lockup { display: flex; flex-direction: column; align-items: stretch; }
  .card--brand .brand-name { font-size: 48px; }
  .card--brand .tagline { font-size: 16px; margin-top: 12px; padding-left: 60px; }
</style>
</head>
<body>
<main class="stage">
  <section class="card card--contact" aria-label="Contact side of business card">
    <div class="contact-block">
      <h2 class="heading">Contact Us</h2>
      <ul class="detail-list">
        <li>012 555 0187</li>
        <li>nargiza.huseynova@velvetlark-example.az</li>
        <li>www.velvetlark-example.az</li>
        <li>17 Samad Str. AZ 1014, Baku, Azerbaijan</li>
      </ul>
    </div>

    <div class="brand-lockup">
      <div class="brand-name"><span class="dot" aria-hidden="true"></span>Velvet &amp; Lark</div>
      <p class="tagline">Happy to make you happy!</p>
    </div>

    <div class="accent-band" aria-hidden="true">
      <span class="dark" style="width:40px"></span>
      <span class="mid" style="width:40px"></span>
      <span class="dark" style="width:40px"></span>
      <span class="light" style="width:40px"></span>
      <span class="dark" style="width:280px"></span>
    </div>

    <div class="social-block">
      <h2 class="heading">Follow Us on Social</h2>
      <ul class="detail-list">
        <li>social-one.example/tulipwanderer</li>
        <li>social-two.example/tulipwanderer</li>
        <li>social-three.example/tulipwanderer</li>
      </ul>
    </div>

    <div class="person">
      <p class="name">Nargiza Huseynova</p>
      <p class="role">General Manager</p>
    </div>
  </section>

  <section class="card card--brand" aria-label="Brand side of business card">
    <div class="brand-lockup">
      <div class="brand-name"><span class="dot" aria-hidden="true"></span>Velvet &amp; Lark</div>
      <p class="tagline">Happy to make you happy!</p>
    </div>
  </section>
</main>
</body>
</html>
```